Carousel for Truck Parts Website

I need three images. 1400 x 1000. They all MUST be made in Adobe Illustrator -- Photoshop not accepted. It needs to be for Ridgeline Rig Supply. We'd like them to be patriotic themed (US flag). One with a announcement of towing/wrecker service 24/7. Call 6203417729. One with a shop online for heavy duty truck parts. Something like "Need Parts? Shop Online. Can't find your part, chat with us." Third would be "we have the one of the largest heavy truck salvage stores in the central United States." Need a part? Call 620-341-7729 and chat with us.

```html
<!DOCTYPE html>
<html lang="en">
<head>
<meta charset="utf-8">
<title>Ridgeline Rig Supply – Carousel</title>
<link href="https://fonts.googleapis.com/css2?family=Poppins:wght@600;700;800&display=swap" rel="stylesheet">
<style>
  :root {
    --page: #ffffff;
    --flag-blue: #0a35b0;
    --flag-red: #f40d0d;
    --white: #ffffff;
    --sky-blue: #1a6ae8;
    --steel-grey: #7b7f86;
    --haze-blue: #4f7fc4;
    --shop-navy: #1d2f8c;
  }
  * { margin: 0; padding: 0; box-sizing: border-box; }
  html, body { width: 1200px; height: 2439px; overflow: hidden; background: var(--page); }
  body { position: relative; font-family: "Poppins", sans-serif; color: var(--white); }

  .slide { position: absolute; left: 176px; width: 846px; height: 604px; overflow: hidden; }
  .slide--towing { top: 185px; }
  .slide--shop { top: 910px; }
  .slide--salvage { top: 1641px; }

  .slide__photo { position: absolute; inset: 0; }
  .slide--towing .slide__photo {
    background:
      radial-gradient(ellipse 45% 50% at 22% 45%, rgba(170,50,45,.75), transparent 70%),
      linear-gradient(160deg, #b9c3cc 0%, #8e9aa6 35%, #6f747c 70%, #5c6067 100%);
  }
  .slide--towing .slide__tint {
    position: absolute; inset: 0;
    background: linear-gradient(200deg, rgba(0,102,255,.95) 0%, rgba(40,110,220,.55) 35%, rgba(120,125,135,.2) 65%, rgba(120,120,125,.5) 100%);
  }
  .slide--shop .slide__photo {
    background:
      radial-gradient(ellipse 60% 30% at 55% 45%, rgba(235,238,242,.85), transparent 70%),
      radial-gradient(ellipse 20% 20% at 10% 55%, rgba(255,225,150,.8), transparent 70%),
      linear-gradient(180deg, #4d8be0 0%, #79a6de 40%, #6d8fbd 65%, #3f5f93 100%);
  }
  .slide--salvage .slide__photo {
    background:
      radial-gradient(ellipse 25% 20% at 72% 64%, rgba(255,240,120,.85), transparent 70%),
      radial-gradient(ellipse 30% 25% at 28% 80%, rgba(40,40,255,.8), transparent 70%),
      linear-gradient(170deg, #1f5fd6 0%, #2b4ca8 30%, #3a4a7c 60%, #25306a 100%);
  }

  .headline { position: absolute; font-weight: 700; line-height: 1; text-shadow: 0 3px 6px rgba(0,0,0,.45); white-space: nowrap; }
  .slide--towing .headline { left: 146px; top: 190px; font-size: 64px; line-height: 78px; }
  .slide--shop .headline { left: 0; width: 846px; text-align: center; top: 252px; font-size: 57px; }
  .slide--salvage .headline { left: 103px; top: 46px; font-size: 29px; line-height: 36px; font-weight: 700; }

  .stripes { position: absolute; display: flex; flex-direction: column; gap: 8px; }
  .stripes span { display: block; height: 11px; background: var(--flag-red); }
  .slide--towing .stripes { left: 570px; top: 272px; width: 130px; }
  .slide--salvage .stripes { left: 0; top: 57px; width: 91px; gap: 7px; }
  .slide--salvage .stripes span { height: 10px; }

  .cta { position: absolute; display: flex; height: 62px; font-weight: 700; white-space: nowrap; }
  .cta__lead, .cta__action { display: flex; align-items: center; justify-content: center; }
  .cta__lead { background: var(--flag-blue); }
  .cta__action { background: var(--flag-red); }
  .slide--towing .cta { left: 161px; top: 364px; font-size: 54px; }
  .slide--towing .cta__lead { width: 149px; }
  .slide--towing .cta__action { width: 363px; }
  .slide--shop .cta { left: 116px; top: 344px; height: 61px; font-size: 33px; }
  .slide--shop .cta__lead { width: 364px; }
  .slide--shop .cta__action { width: 255px; }
  .slide--salvage .cta { left: 148px; top: 239px; height: 61px; font-size: 32px; }
  .slide--salvage .cta__lead { width: 254px; }
  .slide--salvage .cta__action { width: 253px; }

  .phone-line { position: absolute; left: 161px; top: 312px; font-size: 54px; font-weight: 700; text-shadow: 0 3px 6px rgba(0,0,0,.45); letter-spacing: 1px; word-spacing: 18px; }

  .brand { position: absolute; display: flex; align-items: center; gap: 10px; font-size: 22px; font-weight: 700; color: var(--white); white-space: nowrap; }
  .brand__mark { width: 16px; height: 16px; background: var(--white); }
  .slide--towing .brand { left: 245px; top: 472px; }
  .slide--shop .brand { left: 245px; top: 482px; }
  .slide--salvage .brand { left: 238px; top: 462px; }
</style>
</head>
<body>

<section class="slide slide--towing">
  <div class="slide__photo" role="img" aria-label="Red semi truck hauled on a flatbed along a mountain highway, with a faint star pattern"></div>
  <div class="slide__tint"></div>
  <h1 class="headline">Towing/wrecker<br>service 24/7</h1>
  <div class="stripes"><span></span><span></span><span></span></div>
  <div class="cta"><span class="cta__lead">Call</span><span class="cta__action">6203417729</span></div>
  <div class="brand"><span class="brand__mark"></span>Ridgeline Rig Supply</div>
</section>

<section class="slide slide--shop">
  <div class="slide__photo" role="img" aria-label="White semi truck with trailer on a highway under a blue sky, with a faint star pattern"></div>
  <h1 class="headline">Need Parts?&nbsp; Shop Online.</h1>
  <div class="cta"><span class="cta__lead">Can't find your part</span><span class="cta__action">Chat with us.</span></div>
  <div class="brand"><span class="brand__mark"></span>Ridgeline Rig Supply</div>
</section>

<section class="slide slide--salvage">
  <div class="slide__photo" role="img" aria-label="Mechanic in a cap working on a truck engine, tinted blue with a faint star pattern"></div>
  <div class="stripes"><span></span><span></span><span></span></div>
  <h1 class="headline">We have the one of the largest heavy truck<br>salvage stores in the central United States.</h1>
  <div class="cta"><span class="cta__lead">Need a part ?</span><span class="cta__action">Chat with us.</span></div>
  <p class="phone-line">Call 6203417729</p>
  <div class="brand"><span class="brand__mark"></span>Ridgeline Rig Supply</div>
</section>

</body>
</html>
```